TALMORK

The business want a professional looking business card. We have a scetch we will add but want the extra upgrade, and would like more suggestions for variations of our business cards.

```html
<!DOCTYPE html>
<html lang="en">
<head>
<meta charset="utf-8">
<title>Talmork business card</title>
<link href="https://fonts.googleapis.com/css2?family=Hind:wght@400;500;600&display=swap" rel="stylesheet">
<style>
  :root {
    --page-bg: #f6f7f7;
    --card-front: #f7f2e6;
    --card-back-edge: #ebe1cf;
    --card-back-center: #f9f5ec;
    --ink: #4a2c12;
    --gold: #b38c3e;
    --gold-soft: #b89358;
  }
  * { margin: 0; padding: 0; box-sizing: border-box; }
  html, body {
    width: 1200px; height: 670px; overflow: hidden;
    background: var(--page-bg);
    font-family: "Hind", Arial, sans-serif;
  }
  .card {
    position: absolute; top: 178px;
    width: 507px; height: 310px;
  }
  .card-front { left: 68px; background: var(--card-front); color: var(--ink); }
  .card-back {
    left: 630px;
    background: radial-gradient(ellipse at 50% 50%, var(--card-back-center) 0%, var(--card-back-center) 25%, var(--card-back-edge) 100%);
  }
  .holder-name {
    position: absolute; left: 43px; top: 36px;
    font-size: 36px; font-weight: 500; line-height: 1; letter-spacing: 0.2px;
  }
  .holder-title {
    position: absolute; left: 43px; top: 80px;
    font-size: 20px; font-weight: 400; line-height: 1;
  }
  .contact-list { position: absolute; left: 41px; top: 184px; list-style: none; }
  .contact-item {
    display: flex; align-items: center; height: 30.5px;
    font-size: 20px; line-height: 1;
  }
  .contact-icon { width: 20px; height: 20px; margin-right: 14px; flex: none; }
  .brand-lockup {
    position: absolute; left: 336px; top: 112px; width: 150px;
    display: flex; flex-direction: column; align-items: center;
  }
  .brand-dot {
    width: 44px; height: 44px; border-radius: 50%;
    background: var(--gold); margin-bottom: 22px;
  }
  .brand-name-small {
    font-size: 19px; font-weight: 600; letter-spacing: 4px; color: var(--gold); line-height: 1;
  }
  .brand-name-large {
    position: absolute; left: 0; width: 100%; top: 296px; top: 118px;
    text-align: center; padding-left: 16px;
    font-size: 52px; font-weight: 600; letter-spacing: 16px; color: var(--gold); line-height: 1;
  }
  .brand-tagline {
    position: absolute; left: 0; width: 100%; top: 183px;
    text-align: center; padding-left: 9px;
    font-size: 17px; font-weight: 600; letter-spacing: 9px; color: var(--gold-soft); line-height: 1;
  }
</style>
</head>
<body>
  <section class="card card-front">
    <h1 class="holder-name">Anders Holm Lindvik</h1>
    <p class="holder-title">CEO &amp; Founder</p>
    <ul class="contact-list">
      <li class="contact-item">
        <svg class="contact-icon" viewBox="0 0 20 20" aria-hidden="true">
          <rect x="5" y="1" width="10" height="18" rx="2" fill="none" stroke="var(--ink)" stroke-width="1.8"/>
          <circle cx="10" cy="16" r="1" fill="var(--ink)"/>
        </svg>004791234567
      </li>
      <li class="contact-item">
        <svg class="contact-icon" viewBox="0 0 20 20" aria-hidden="true">
          <rect x="1" y="4" width="18" height="12" fill="var(--ink)"/>
          <path d="M1 4 L10 11 L19 4 M1 16 L8 9.5 M19 16 L12 9.5" fill="none" stroke="var(--card-front)" stroke-width="1.2"/>
        </svg>talmork.llc@postmail.com
      </li>
      <li class="contact-item">
        <svg class="contact-icon" viewBox="0 0 20 20" aria-hidden="true">
          <circle cx="10" cy="10" r="8.5" fill="none" stroke="var(--ink)" stroke-width="1.3"/>
          <ellipse cx="10" cy="10" rx="4" ry="8.5" fill="none" stroke="var(--ink)" stroke-width="1"/>
          <path d="M1.5 10 H18.5 M3 6 H17 M3 14 H17" stroke="var(--ink)" stroke-width="1"/>
        </svg>www.talmork.llc
      </li>
    </ul>
    <div class="brand-lockup">
      <span class="brand-dot"></span>
      <span class="brand-name-small">TALMORK</span>
    </div>
  </section>

  <section class="card card-back">
    <p class="brand-name-large">TALMORK</p>
    <p class="brand-tagline">SINCE 2026</p>
  </section>
</body>
</html>
```